Newspaper Ad - New Veterinarian Introduction

I am looking to create a standard Newspaper ad that l can use as a template to introduce new Veterinarians (when they join our practice) to the local community.

The goal is to create an ad that captures the reader's eye, creates a warm emotional connection with the vet, and that encourages the reader to think of our clinic when they have veterinary needs.

Target Market(s)

Pet owners

Industry/Entity Type

Veterinary

Requirements
Must have
• The ad will contain a photo of the vet (sample phone attached) and a short bio of their interests and/or specialties.

The ad will also include basic contact information on the clinic: logo, phone, website, email
Nice to have
• Optional information could include:
- Like us on linkaroo
- features of the clinic (e.g. feline friendly room)
- other vets who work at the clinic

```html
<!DOCTYPE html>
<html lang="en">
<head>
<meta charset="utf-8">
<title>Willow Creek Animal Hospital – New Veterinarian</title>
<link rel="stylesheet" href="https://fonts.googleapis.com/css2?family=Arimo:wght@400;700&display=swap">
<style>
  :root {
    --brand-blue: #1a8fd0;
    --names-blue: #2f6fb7;
    --text: #222222;
    --paper: #ffffff;
    --photo-light: #c98a6a;
    --photo-dark: #5b4a3e;
    --puppy-light: #e8d2b4;
    --puppy-mid: #b9865a;
    --basket-dark: #3d2c20;
  }
  * { box-sizing: border-box; margin: 0; padding: 0; }
  html, body { width: 702px; height: 1200px; overflow: hidden; background: var(--paper); }
  body { font-family: "Arimo", Arial, sans-serif; color: var(--text); }
  .ad { position: relative; width: 702px; height: 1200px; background: var(--paper); }

  .brand {
    position: absolute; left: 72px; top: 40px;
    display: flex; align-items: center; gap: 16px;
  }
  .brand-dot { width: 78px; height: 78px; border-radius: 50%; background: var(--brand-blue); }
  .brand-name {
    font-weight: 700; font-size: 29px; line-height: 1.05; color: var(--brand-blue);
    text-transform: uppercase; letter-spacing: 0.5px; width: 240px;
  }

  .vet-photo {
    position: absolute; left: 64px; top: 187px; width: 176px; height: 184px;
    background: linear-gradient(160deg, var(--photo-light), var(--photo-dark));
  }
  .bio {
    position: absolute; left: 303px; top: 186px; width: 392px;
    font-size: 19px; line-height: 21px;
  }
  .welcome {
    position: absolute; left: 59px; top: 396px; width: 236px;
    font-size: 19px; line-height: 21px;
  }
  .lower-copy {
    position: absolute; left: 59px; top: 524px; width: 625px;
    display: flex; flex-direction: column; gap: 14px;
    font-size: 19px; line-height: 23px;
  }
  .team { color: var(--names-blue); margin-top: -6px; }

  .puppies {
    position: absolute; left: 64px; top: 760px; width: 570px; height: 360px;
    border-radius: 40% 40% 48% 48% / 30% 30% 40% 40%;
    background: linear-gradient(180deg, var(--puppy-light) 0%, var(--puppy-mid) 45%, var(--basket-dark) 80%);
  }
  .contact {
    position: absolute; left: 0; width: 702px; top: 1032px;
    text-align: center; color: var(--paper); font-weight: 700; font-style: normal;
    font-size: 20px; line-height: 1.3;
  }
  .social {
    position: absolute; right: 36px; top: 1092px;
    display: flex; flex-direction: column; align-items: flex-end; gap: 10px;
  }
  .social-square { width: 54px; height: 54px; background: var(--names-blue); margin-right: 4px; }
  .social-label { font-size: 18px; color: var(--names-blue); }
</style>
</head>
<body>
<main class="ad">
  <header class="brand">
    <span class="brand-dot"></span>
    <span class="brand-name">Willow Creek Animal Hospital</span>
  </header>

  <div class="vet-photo" role="img" aria-label="Portrait of Dr. Hannah Pierce holding a small rabbit"></div>

  <p class="bio">Graduating from the Prairie College of Veterinary Medicine in Saskatoon in 2002, Dr. Pierce has over 10 years of veterinary experience. Her love and care for animals extends beyond work to her home and through her volunteer work at the local wildlife rehabilitation centre. Dr. Pierce loves the challenges and diversity that a general veterinary clinic brings and has a special interest in internal medicine, dentistry and improving the quality of life for aging pets.</p>

  <p class="welcome">Willow Creek Animal Hospital is pleased to welcome Dr. Hannah Pierce to our practice.</p>

  <div class="lower-copy">
    <p class="reassure">So whether your companion is<br>&nbsp;You can rest assured your pet is in good hands with Dr. Pierce.</p>
    <p class="news">Willow Creek now has a linkaroo page where you can follow interesting stories and see patient experiences. Sign on and “Like” us today. Feline Friendly Room At Willow Creek we appreciate how stressful a visit to the Vet can be to a cat...we now have a Feline Friendly Room.</p>
    <p class="team">Dr. Maren Holt, Dr. Lena Varga,<br>Dr. Corin Baxley, and Dr. Anita Moravec</p>
  </div>

  <div class="puppies" role="img" aria-label="Litter of bulldog puppies sitting in a wicker basket"></div>

  <address class="contact">
    Ph: 780-555-0142<br>
    Email: info@willowcreekvet.com<br>
    www.willowcreekvet.com
  </address>

  <div class="social">
    <span class="social-square"></span>
    <span class="social-label">Like us on linkaroo</span>
  </div>
</main>
</body>
</html>
```